Single brochure for international companies in the financial sector

We need to update a brochure 4 pages presenting our company. We are a financial engineering company. The final design must provide financial security, service and trust. you will find the current brochure copy. Our color code is Orange (RGB 235/100/68), Black, White and Gray. photos show the visual of the site, but it is not mandatory to keep them.

Target Market(s)

wealth management professionals

Industry/Entity Type

Finance

Requirements
Must have
• Logo Tolvane Capital all text in the document color Orange Tolvane (RGB 235/100/68)
Nice to have
• Vista Font
Should not have
• images / pictures of people

```html
<!DOCTYPE html>
<html lang="en">
<head>
<meta charset="utf-8">
<title>Tolvane Capital – Our Services</title>
<link rel="stylesheet" href="https://fonts.googleapis.com/css2?family=Didact+Gothic&display=swap">
<style>
  :root {
    --orange: rgb(235, 100, 68);
    --orange-soft: #f07a5c;
    --ink: #2b2b2b;
    --text: #555555;
    --rule: #4a4a4a;
    --white: #ffffff;
    --stone-dark: #2e2e2e;
    --stone-mid: #8a8a8a;
    --sky: #c9c9c9;
  }
  * { margin: 0; padding: 0; box-sizing: border-box; }
  html, body {
    width: 785px;
    height: 1200px;
    overflow: hidden;
    background: var(--white);
  }
  .page {
    position: relative;
    width: 785px;
    height: 1200px;
    background: var(--white);
    font-family: "Didact Gothic", "Helvetica Neue", Arial, sans-serif;
    color: var(--text);
  }
  .hero {
    position: absolute;
    left: 0; top: 0;
    width: 785px; height: 262px;
    background: linear-gradient(125deg, var(--stone-mid) 0%, var(--stone-dark) 30%, var(--sky) 50%, var(--stone-mid) 75%, var(--sky) 100%);
  }
  .hero-rule {
    position: absolute;
    left: 0; top: 259px;
    width: 785px; height: 3px;
    background: var(--orange);
  }
  .page-title {
    position: absolute;
    left: 392px; top: 196px;
    width: 393px; height: 66px;
    background: linear-gradient(90deg, var(--orange) 0%, var(--orange-soft) 50%, var(--orange) 100%);
    color: var(--white);
    font-size: 38px;
    font-weight: 400;
    line-height: 66px;
    text-align: center;
    letter-spacing: 0.5px;
  }
  .service {
    position: absolute;
    left: 58px;
    width: 670px;
  }
  .service h2 {
    font-size: 24px;
    font-weight: 400;
    color: var(--ink);
    line-height: 1;
    margin-bottom: 26px;
  }
  .service p {
    font-size: 15.5px;
    line-height: 30px;
    letter-spacing: 0.6px;
    text-align: justify;
    margin-bottom: 12px;
  }
  .service--advice { top: 384px; }
  .service--portfolio { top: 617px; }
  .service--partners { top: 871px; }
  .footer {
    position: absolute;
    left: 0; top: 1122px;
    width: 785px;
    display: flex;
    align-items: center;
  }
  .footer-rule {
    height: 1px;
    background: var(--rule);
    flex: 0 0 230px;
  }
  .footer-name {
    flex: 1;
    text-align: center;
    color: var(--orange);
    font-size: 17px;
    letter-spacing: 5px;
    text-transform: uppercase;
  }
</style>
</head>
<body>
<div class="page">
  <div class="hero" role="img" aria-label="Black and white photograph of a stone aqueduct arch against the sky"></div>
  <div class="hero-rule"></div>
  <h1 class="page-title">OUR SERVICES</h1>

  <section class="service service--advice">
    <h2>Investment Advice</h2>
    <p>Each client is looking for a unique investment solution. Hence, we combine internal and external resources to create the financial product that will best fit our clients requirements.</p>
    <p>Thanks to a truly independent advice, we offer bespoke, simple and efficient solutions.</p>
  </section>

  <section class="service service--portfolio">
    <h2>Portfolio Analysis</h2>
    <p>We advise our clients on their portfolios of financial products. Together we identify the needs for restructuring or reallocating the assets.</p>
    <p>We also provide full monitoring and reporting services throughout the life of the products.</p>
  </section>

  <section class="service service--partners">
    <h2>Partner Selection</h2>
    <p>Our internal tools allow us to continuously assess the issuers we are working with.</p>
    <p>Therefore we give our clients the luxury to chose among the best issuers for their investment solution.</p>
  </section>

  <footer class="footer">
    <span class="footer-rule"></span>
    <span class="footer-name">Tolvane Capital</span>
    <span class="footer-rule"></span>
  </footer>
</div>
</body>
</html>
```